Bookcover: Lessons From the Silent Orchard

I am publishing a super-low-cost innovation book for €4,99 on Bravolo Self Release to help everyone become a great innovator: young ambitious people without college education nor a big budget. Do you want to help me?

Brief:
Design a book cover 1600 x 2560 pixels for BSR.
Main title: Lessons From the Silent Orchard
Sub title: mindset - insights - skills & tools
Author: Maarten de Klerk
Design: captive, and appealing to everyone
Target Group: young ambitious people without college education

For bravolo please format the height/width ratio of 1.6:1

```html
<!DOCTYPE html>
<html lang="en">
<head>
<meta charset="utf-8">
<title>Lessons From the Silent Orchard — Book Cover</title>
<link href="https://fonts.googleapis.com/css2?family=Chakra+Petch:wght@700&family=Inter:wght@400&display=swap" rel="stylesheet">
<style>
  :root {
    --backdrop: #ece9e4;
    --cover-white: #ffffff;
    --ink: #2b2b2b;
    --ink-soft: #333333;
    --art-tone-a: #8a7bb0;
    --art-tone-b: #6fa8a2;
    --art-tone-c: #e2c56a;
  }
  * { margin: 0; padding: 0; box-sizing: border-box; }
  html, body {
    width: 1200px;
    height: 1200px;
    overflow: hidden;
    background: var(--backdrop);
  }
  .canvas {
    position: relative;
    width: 1200px;
    height: 1200px;
  }
  .book-cover {
    position: absolute;
    left: 274px;
    top: 102px;
    width: 652px;
    height: 996px;
    background: var(--cover-white);
    text-align: center;
  }
  .book-title {
    position: absolute;
    left: 0;
    right: 0;
    top: 54px;
    font-family: "Chakra Petch", sans-serif;
    font-weight: 700;
    font-size: 108px;
    line-height: 111px;
    letter-spacing: 1px;
    text-transform: uppercase;
    color: var(--ink);
  }
  .book-title span { display: block; white-space: nowrap; }
  .book-subtitle {
    position: absolute;
    left: 0;
    right: 0;
    top: 512px;
    font-family: "Inter", sans-serif;
    font-weight: 400;
    font-size: 29px;
    line-height: 36px;
    color: var(--ink-soft);
  }
  .cover-art {
    position: absolute;
    left: 151px;
    top: 578px;
    width: 350px;
    height: 280px;
    border-radius: 24px;
    background: linear-gradient(135deg, var(--art-tone-a), var(--art-tone-b) 55%, var(--art-tone-c));
    opacity: 0.85;
  }
  .book-author {
    position: absolute;
    left: 0;
    right: 0;
    top: 912px;
    font-family: "Chakra Petch", sans-serif;
    font-weight: 700;
    font-size: 36px;
    line-height: 44px;
    letter-spacing: 1px;
    text-transform: uppercase;
    color: var(--ink);
  }
</style>
</head>
<body>
  <main class="canvas">
    <article class="book-cover">
      <h1 class="book-title">
        <span>Lessons</span>
        <span>From the</span>
        <span>Silent</span>
        <span>Orchard</span>
      </h1>
      <p class="book-subtitle">Mindset - Insights - Skills &amp; Tools</p>
      <div class="cover-art" role="img" aria-label="Cover artwork: colourful crayons arranged in a circle, joined by a thin network of dots and lines"></div>
      <p class="book-author">Maarten de Klerk</p>
    </article>
  </main>
</body>
</html>
```